It is a leisure sector investment company.The company plans to invest in a luxurious 5 star resort

We need a stationery design to our company 'Copper Lantern Limited' using the winning logo design. We need the letter heads, envelopes & the business cards. Should be simple, plain and professional
We have upload the source file & vector files which gives our logo design. We prefer the bottom logo.

Have updated under 'must have priorities', the company name, address, tel no. fax no. & the company reg no. which should come on the letter head. the long envelope should have the company name, tel & fax no. 
Business card should have the company name, name on the card, designation, tel no. fax no.  

- Letter head details:
Copper Lantern Limited
14 Floor, South Wing, Halvard Merchant Plaza,
Merrow Court, Colombo 01, Sri Lanka
Tel: +94 11 5047293 Fax: +94 11 5047298
Company Reg No.QX 6142
Long Envelope should have only the company name, adress, Tel & Fax
Business Cards should have the company name, Tel & Fax:
Business Card 1 - Lasantha Gunaratne - Chairman
Business Card 2 - Nimal.T.Wijesooriya - COO

```html
<!DOCTYPE html>
<html lang="en">
<head>
<meta charset="utf-8">
<title>Copper Lantern Limited — Stationery Set</title>
<link href="https://fonts.googleapis.com/css2?family=Questrial&display=swap" rel="stylesheet">
<style>
:root{
  --brown:#4a3d36;
  --lime:#b6d334;
  --leaf:#8dbf2e;
  --paper:#ffffff;
  --ink:#3a3a3a;
  --grey:#8a8a8a;
  --backdrop:#e9e6e1;
  --font:"Questrial", "Century Gothic", sans-serif;
}
*{box-sizing:border-box;margin:0;padding:0}
html,body{width:1200px;height:900px;overflow:hidden}
body{background:var(--backdrop);font-family:var(--font);color:var(--ink);position:relative}
.sheet{position:absolute;background:var(--paper);box-shadow:0 2px 8px rgba(0,0,0,.15);overflow:hidden}

/* shared pieces */
.stripes-h{position:absolute;left:0;right:0;top:0}
.stripes-h .thick{height:7px;background:var(--lime)}
.stripes-h .thin{height:2px;background:var(--leaf);margin-top:3px}
.logo-name{font-family:var(--font);text-transform:uppercase;letter-spacing:.06em;line-height:1.15;color:var(--brown)}
.logo-name.on-dark{color:var(--paper)}
.contact{font-size:9px;color:var(--grey);line-height:1.5}
.stripes-v{position:absolute;top:0;bottom:0;display:flex;gap:3px}
.stripes-v span{display:block;width:5px;background:var(--lime)}
.stripes-v span.thin{width:2px;background:var(--leaf)}

/* letterhead */
.letterhead{left:40px;top:60px;width:530px;height:780px}
.letterhead .logo-name{position:absolute;left:42px;top:40px;font-size:17px}
.letterhead .contact{position:absolute;right:160px;top:30px}
.letter-body{position:absolute;left:42px;top:140px;width:440px;font-size:10.5px;line-height:1.6}
.letter-body p{margin-bottom:13px}
.letter-band{position:absolute;left:0;right:0;bottom:58px;height:76px;background:var(--brown)}
.letter-band .stripes-v{left:8px}
.letter-band .address{position:absolute;right:32px;top:12px;text-align:right;color:#e8e2dc;font-size:10px;line-height:1.55}
.letter-band .address strong{color:var(--paper);font-weight:400;font-size:11px}
.company-reg{position:absolute;right:32px;bottom:38px;font-size:9px;color:var(--grey)}

/* envelope back */
.envelope-back{left:610px;top:50px;width:570px;height:200px}
.envelope-back svg{position:absolute;left:0;top:0}
.envelope-back .logo-name{position:absolute;left:0;right:0;top:30px;text-align:center;font-size:17px}

/* envelope front */
.envelope-front{left:610px;top:280px;width:570px;height:210px}
.envelope-band{position:absolute;left:0;right:0;bottom:0;height:58px;background:var(--brown);color:#e8e2dc;font-size:9.5px;line-height:1.5}
.envelope-band .phones{position:absolute;left:200px;top:13px}
.envelope-band .divider{position:absolute;left:300px;top:10px;bottom:10px;width:1px;background:var(--lime)}
.envelope-band .address{position:absolute;right:24px;top:8px;text-align:right}
.envelope-band .address strong{color:var(--paper);font-weight:400;font-size:10.5px}

/* business cards */
.card{width:280px;height:165px}
.card-front{left:610px;top:540px}
.card-front .logo-name{position:absolute;left:14px;top:22px;font-size:11px}
.card-front .contact{position:absolute;right:16px;top:12px;font-size:8.5px}
.name-band{position:absolute;left:0;top:66px;width:232px;height:40px;background:var(--brown);padding:5px 0 0 54px}
.name-band .holder{color:var(--paper);font-size:15px;letter-spacing:.01em}
.name-band .title{color:#d9d1ca;font-size:8.5px}
.card-front .stripes-v{left:232px;top:60px;bottom:auto;height:52px}
.card-front .company-line{position:absolute;right:14px;bottom:34px;color:var(--leaf);font-size:11px;letter-spacing:.03em;text-transform:uppercase}

.card-back{left:900px;top:540px;background:var(--brown)}
.card-back .stripes-v{left:10px}
.card-back .logo-name{position:absolute;left:30px;right:0;top:66px;text-align:center;font-size:15px}
</style>
</head>
<body>

<section class="sheet letterhead" aria-label="Letterhead">
  <div class="stripes-h"><div class="thick"></div><div class="thin"></div></div>
  <div class="logo-name">Copper Lantern<br>Limited</div>
  <div class="contact">Tel: +94 11 5047293<br>Fax: +94 11 5047298</div>
  <div class="letter-body">
    <p>(Date)</p>
    <p>(Address)</p>
    <p>Dear (Name),</p>
    <p>This is a sample letter that has been placed to demonstrate the typing format on the (Your Company) letterhead design. When positioned properly, it will serve to work in harmony with the other elements on the letterhead.</p>
    <p>This letterhead design is meant to project an image of professionalism and reliability. By using alignments we have created a very spacious feeling. The simplicity suggests strength and the clean lines contribute to the aesthetics of the layout. These basic qualities along with the (Your Company) colours, are consistent with the overall look and helps to reinforce the (Your Company) brand.</p>
    <p>This letterhead design is based on the (Form of your logo) from the (Your Company) logo. Each piece of stationery has a part of the (Form of your logo). Together, they form a perfect (Form of your logo) which become a strong design element of the (Your Company) brand.</p>
    <p>Sincerely yours,</p>
    <p>(Signature)</p>
    <p>(Name)<br>Creative Director</p>
  </div>
  <div class="letter-band">
    <div class="stripes-v"><span></span><span class="thin"></span></div>
    <div class="address"><strong>Copper Lantern Limited</strong><br>14 Floor, South Wing, Halvard Merchant Plaza,<br>Merrow Court, Colombo 01, Sri Lanka</div>
  </div>
  <div class="company-reg">Company Reg No.QX 6142</div>
</section>

<section class="sheet envelope-back" aria-label="Envelope back">
  <svg width="570" height="200" viewBox="0 0 570 200" aria-hidden="true">
    <path d="M0 0 H570 V20 Q 300 125 285 125 Q 270 125 0 20 Z" fill="var(--brown)"/>
  </svg>
  <div class="logo-name on-dark">Copper Lantern<br>Limited</div>
</section>

<section class="sheet envelope-front" aria-label="Envelope front">
  <div class="stripes-h"><div class="thick"></div><div class="thin"></div></div>
  <div class="envelope-band">
    <div class="phones">Tel: +94 11 5047293<br>Fax: +94 11 5047298</div>
    <div class="divider"></div>
    <div class="address"><strong>Copper Lantern Limited</strong><br>14 Floor, South Wing, Halvard Merchant Plaza,<br>Merrow Court, Colombo 01, Sri Lanka</div>
  </div>
</section>

<section class="sheet card card-front" aria-label="Business card front">
  <div class="logo-name">Copper Lantern<br>Limited</div>
  <div class="contact">Tel: +94 11 5047293<br>Fax: +94 11 5047298</div>
  <div class="name-band">
    <div class="holder">Lasantha Gunaratne</div>
    <div class="title">Chairman</div>
  </div>
  <div class="stripes-v"><span></span><span class="thin"></span></div>
  <div class="company-line">Copper Lantern Limited</div>
</section>

<section class="sheet card card-back" aria-label="Business card back">
  <div class="stripes-v"><span></span><span class="thin"></span></div>
  <div class="logo-name on-dark">Copper Lantern<br>Limited</div>
</section>

</body>
</html>
```